Maple Tide Events
MaplTideEvents - Business Card/Stationary
I need double sided standard sized Business Card [3.5" x 2"]
we use "segan" on the website - feel free to expirement, we are not set on one yet
Professional
Nadia Feltwick
Director of Logistics
4187 Birchwell Hollow Lane
Soquel, CA 95182
nadia@mapletide.com
www.mapletide.com
-Please look at our website: www.mapletide.com
We would like the business card to replicate the look of the website.
-As noted earlier, we have not settled on a font yet, please feel free to be creative with the styles
- Font used on website = segan (or similar)
-Double-Sided is "optional" we would also like to see just some single sided versions as well.
- Regular standard size business card
we wanted to explore the option of having a double sided card. This is not mandatory, but if there is a creative design for it, this would be great.
Logo - Icon ONLY
Logo - Icon with Title

```html
<!DOCTYPE html>
<html lang="en">
<head>
<meta charset="utf-8">
<title>Maple Tide Events – Business Card</title>
<link rel="stylesheet" href="https://fonts.googleapis.com/css2?family=Arimo:wght@400;700&display=swap">
<style>
  :root {
    --page: #ffffff;
    --blue-deep: #2b4b8c;
    --blue-mid: #2f6fb3;
    --blue-light: #3ba3dc;
    --white: #ffffff;
    --edge: #1f3a6e;
  }
  * { margin: 0; padding: 0; box-sizing: border-box; }
  html, body {
    width: 1200px; height: 732px; overflow: hidden;
    background: var(--page);
    font-family: "Arimo", Arial, sans-serif;
  }
  .canvas { position: relative; width: 1200px; height: 732px; }

  .brand { position: absolute; display: flex; align-items: center; }
  .brand-mark { flex: none; border-radius: 50%; }
  .brand-text { display: flex; flex-direction: column; margin-left: 14px; }
  .brand-name { font-weight: 400; line-height: 1; white-space: nowrap; }
  .brand-tagline { font-size: 13px; line-height: 1.2; margin-top: 5px; white-space: nowrap; }

  .card-front {
    position: absolute; left: 0; top: 156px;
    width: 732px; height: 415px;
    background: linear-gradient(90deg, var(--blue-deep) 0%, var(--blue-mid) 50%, var(--blue-light) 100%);
    border: 1px solid var(--edge);
  }
  .card-front .brand { left: 24px; top: 310px; }
  .card-front .brand-mark { width: 76px; height: 76px; background: var(--white); }
  .card-front .brand-name { font-size: 34px; color: var(--white); }
  .card-front .brand-tagline { color: var(--white); }

  .card-back {
    position: absolute; left: 792px; top: 0;
    width: 408px; height: 728px;
    border: 1px solid var(--edge);
    background: linear-gradient(180deg, var(--blue-light) 0%, var(--blue-mid) 45%, var(--blue-deep) 100%);
  }
  .card-back .header { position: absolute; left: 0; top: 0; width: 100%; height: 144px; background: var(--white); }
  .card-back .brand { left: 28px; top: 32px; }
  .card-back .brand-mark { width: 78px; height: 78px; background: var(--blue-mid); }
  .card-back .brand-name { font-size: 30px; color: var(--blue-mid); }
  .card-back .brand-tagline { color: var(--blue-mid); }

  .contact-name {
    position: absolute; left: 19px; top: 276px;
    font-size: 29px; font-weight: 700; color: var(--white);
  }
  .contact-title {
    position: absolute; left: 19px; top: 314px;
    font-size: 26px; font-weight: 400; color: var(--white);
  }
  .contact-lines {
    position: absolute; left: 19px; top: 636px;
    list-style: none; color: var(--white); font-size: 19px; line-height: 44px;
  }
</style>
</head>
<body>
<main class="canvas">
  <section class="card-front" aria-label="Business card front">
    <div class="brand">
      <span class="brand-mark" aria-hidden="true"></span>
      <div class="brand-text">
        <span class="brand-name">Maple Tide Events</span>
        <span class="brand-tagline">plans that come together</span>
      </div>
    </div>
  </section>

  <section class="card-back" aria-label="Business card back">
    <div class="header">
      <div class="brand">
        <span class="brand-mark" aria-hidden="true"></span>
        <div class="brand-text">
          <span class="brand-name">Maple Tide Events</span>
          <span class="brand-tagline">plans that come together</span>
        </div>
      </div>
    </div>
    <h1 class="contact-name">Nadia Feltwick</h1>
    <p class="contact-title">Director of Logistics</p>
    <ul class="contact-lines">
      <li class="phone">Ph: (555) 318.7042</li>
      <li class="email">nadia@mapletide.com</li>
    </ul>
  </section>
</main>
</body>
</html>
```